New Design for our Velintor Gran Reserva Brandy, it is the label design for the bottle label

We need a new bottle label for our Brandy Gran Reserva that we want to bring to the market.

Please have a look at all our current bottles and labels and the feel of our company under www.velintor-example.ch

The bottle that we will be using for the brand is a different one than the one that we already have, the design of the bottle is attached with a document.

I have also attached a briefing in regards to Brandy in general for your information.

### 1. What is Brandy?
Brandy is a distilled spirit made from fermented wine or other fruit wines. It is traditionally aged in oak barrels, which gives it its characteristic color and rich flavor. The aging process in oak is essential for developing the aromas and quality of the brandy.

### 2. What is Brandy Reserva?
A Brandy labeled as "Reserva" has undergone a longer aging process, typically at least 2 to 3 years, in oak barrels. This aging gives the brandy a deeper, more complex flavor profile and a darker color. "Reserva" is often an indication of higher quality.

### 3. Who enjoys drinking Brandy?
Brandy is typically favored by those who appreciate a deep, rich tasting experience. This often includes older consumers who value the time-aged complexity of the spirit. However, Brandy is also gaining popularity among younger people, especially through cocktails and modern serving styles.

### 4. Why is Brandy trending?
Brandy is experiencing a resurgence as consumers increasingly value quality and artisanal production methods. Its versatility in cocktails and association with traditional, luxurious experiences have also contributed to its renewed popularity.

### 5. What colors would be associated with Brandy?
The typical colors associated with Brandy are warm gold, amber, and deep golden-brown tones. These colors reflect the aging process in oak barrels and the richness of the flavors. Other associated colors might include dark brown and mahogany.

### 6. What is important to customers when buying Brandy?
Customers care about the origin of the Brandy, the aging time, the quality of the ingredients, the production method, and the brand. They also pay attention to the prestige of the product and the authenticity of the production.

### 7. What is not important to customers when buying Brandy?
For many customers, the price and packaging (unless it’s especially exclusive) may be less important than the quality and taste of the Brandy. The distillery name might be less significant if it isn’t tied to a particular reputation.

### 8. What do customers know about Swiss Brandy?
Swiss Brandy is still relatively unknown in many markets, but customers who are familiar with it appreciate the precision and quality of Swiss production. Swiss Brandy is assumed to be made with care and under strict quality standards.

### 9. What is Brandy Gran Reserva?
**Brandy Gran Reserva** is an even higher quality and longer-aged version of Brandy. Generally, a Gran Reserva is aged for at least 5 to 10 years or more in oak barrels. This extended aging process gives the Brandy an especially deep, complex flavor profile and often a darker, richer color. Gran Reserva is often regarded as the top-tier product within a Brandy range and appeals to discerning consumers who value quality, refinement, and a luxurious tasting experience.

The label “Gran Reserva” thus indicates the highest quality level for Brandies, similar to other spirits (like wine or whisky), where the aging time is a critical factor.

### 10. What emotions are associated with Brandy?
Brandy is often associated with luxury, relaxation, and comfort. It evokes feelings of tradition, elegance, and sophistication. Drinking Brandy is frequently seen as a moment of reflection and enjoyment.

### 11. How should Brandy be marketed?
Brandy should be marketed with a focus on its artisanal production, quality, and tradition. A narrative around the product, its aging, and origin can help create an emotional connection with the customer. The marketing should also emphasize the versatility of Brandy, whether consumed neat or in cocktails.

### 12. Sales test and label design for Velintor Brandy
For a sales test, I would suggest a tasting in an upscale setting, perhaps paired with a storytelling presentation highlighting the history of the 6-year aged Brandy and its aging in oak barrels.

**Label design**:
The label should reflect the exclusivity of the product, with an elegant, minimalist design. Colors like deep gold, mahogany, and a hint of deep blue could be used to emphasize the aging and quality of the Brandy. The label should include information about the aging time, the use of oak barrels, and a brief story about the Brandy’s production. A seal or embossing highlighting the craftsmanship would also be fitting.

Target Market(s)

Customers that like Brandy

Requirements
Must have
• the Alcohol % must be included on the label as well as our address.

```html
<!DOCTYPE html>
<html lang="en">
<head>
<meta charset="utf-8">
<title>Velintor Gran Reserva Brandy – Label</title>
<link href="https://fonts.googleapis.com/css2?family=Cinzel:wght@400;600;700&family=EB+Garamond:ital,wght@0,400;1,400&display=swap" rel="stylesheet">
<style>
  :root {
    --page: #f4f3f0;
    --black-band: #15120e;
    --green: #0a2a20;
    --gold: #b8923f;
    --gold-light: #d9b76a;
    --cream: #efe9dc;
    --ink: #6b6458;
    --ink-soft: #8d877b;
    --wax: #a5161b;
    --silver: #c9c9c9;
  }
  * { margin: 0; padding: 0; box-sizing: border-box; }
  html, body { width: 1200px; height: 1200px; overflow: hidden; }
  body { background: var(--page); position: relative; font-family: "EB Garamond", serif; }

  /* Neck label */
  .neck-label {
    position: absolute; left: 150px; top: 340px; width: 125px; height: 522px;
    border-radius: 8px; overflow: hidden; background: var(--cream);
  }
  .neck-band {
    position: absolute; left: 0; top: 0; width: 100%; height: 375px; background: var(--black-band);
    mask: conic-gradient(from -45deg at bottom, #0000, #000 1deg 89deg, #0000 90deg) bottom / 8px 51% repeat-x,
          linear-gradient(#000, #000) top / 100% 50% no-repeat;
  }
  .neck-title {
    position: absolute; left: 50%; top: 187px; transform: translate(-50%, -50%) rotate(-90deg);
    white-space: nowrap; font-family: "Cinzel", serif; font-weight: 700; font-size: 30px;
    letter-spacing: 2px; color: var(--gold);
  }
  .neck-sub {
    position: absolute; top: 405px; width: 100%; text-align: center;
    font-family: "Cinzel", serif; font-size: 11px; line-height: 11px; color: var(--gold); font-weight: 600;
  }
  .neck-script {
    position: absolute; left: 17px; top: 440px; width: 90px; height: 50px; border-radius: 4px;
    background: linear-gradient(90deg, #e6e1d6, #d2cdc3, #e6e1d6);
  }

  /* Main label */
  .main-label {
    position: absolute; left: 330px; top: 186px; width: 760px; height: 830px;
    border-radius: 15px; overflow: hidden; background: var(--green);
  }
  .brand-band {
    position: absolute; left: 0; top: 0; width: 100%; height: 205px; background: var(--black-band);
    border-bottom: 4px solid var(--gold);
  }
  .origin-square {
    position: absolute; left: 361px; top: 38px; width: 38px; height: 24px; background: #d5202a;
  }
  .brand-name {
    position: absolute; top: 76px; width: 100%; text-align: center;
    font-family: "Cinzel", serif; font-weight: 700; font-size: 50px; color: var(--gold-light); letter-spacing: 1px;
  }
  .brand-tag {
    position: absolute; top: 143px; width: 100%; text-align: center;
    font-family: "Cinzel", serif; font-size: 12px; letter-spacing: 1.5px; color: #e8e4da;
  }
  .product-title {
    position: absolute; top: 253px; width: 100%; text-align: center;
    font-family: "Cinzel", serif; font-weight: 700; font-size: 48px; letter-spacing: 3px; color: var(--gold);
  }
  .product-sub {
    position: absolute; top: 320px; width: 100%; text-align: center;
    font-family: "Cinzel", serif; font-size: 19px; letter-spacing: 2px; color: var(--gold);
  }
  .script-word {
    position: absolute; left: 240px; top: 355px; width: 280px; height: 125px; border-radius: 8px;
    background: radial-gradient(ellipse at center, rgba(220,220,220,0.22), rgba(220,220,220,0.04) 70%, transparent);
  }

  .info-card {
    position: absolute; left: 101px; top: 516px; width: 560px; height: 206px; background: var(--cream);
    mask: conic-gradient(from -45deg at bottom, #0000, #000 1deg 89deg, #0000 90deg) bottom / 8px 51% repeat-x,
          conic-gradient(from 135deg at top, #0000, #000 1deg 89deg, #0000 90deg) top / 8px 51% repeat-x;
  }
  .story {
    position: absolute; left: 30px; top: 22px; width: 205px;
    font-style: italic; font-size: 11.5px; line-height: 18px; color: var(--ink-soft);
  }
  .age-mark {
    position: absolute; left: 245px; top: 18px; width: 70px; text-align: center;
    font-family: "Cinzel", serif; color: var(--gold); font-weight: 600;
  }
  .age-mark .age-word { font-size: 17px; line-height: 18px; display: block; }
  .age-mark .age-num { font-family: "EB Garamond", serif; font-size: 54px; line-height: 46px; color: #4a4640; display: block; }
  .tasting {
    position: absolute; left: 330px; top: 22px; width: 215px; list-style: none;
    font-style: italic; font-size: 11.5px; line-height: 19.5px; color: var(--ink-soft);
  }
  .tasting b { font-weight: 400; color: var(--ink); }
  .barrel-line {
    position: absolute; top: 133px; width: 100%; text-align: center;
    font-family: "Cinzel", serif; font-size: 15px; letter-spacing: 1px; color: var(--ink-soft);
    display: flex; justify-content: center; align-items: center; gap: 8px; padding-right: 40px;
  }
  .barrel-icon { width: 42px; height: 36px; border-radius: 8px; background: linear-gradient(#bdb8ae, #8f8a80); }
  .volume {
    position: absolute; top: 174px; width: 100%; text-align: center; padding-right: 40px;
    font-family: "Cinzel", serif; font-size: 13px; letter-spacing: 1px; color: var(--gold); font-weight: 600;
  }
  .wax-seal {
    position: absolute; left: 557px; top: 625px; width: 100px; height: 100px; border-radius: 50%;
    background: radial-gradient(circle at 40% 35%, #c72a2c, var(--wax) 55%, #6e0c10);
  }
  .producer {
    position: absolute; top: 766px; width: 100%; text-align: center;
    font-family: "Cinzel", serif; font-size: 13px; letter-spacing: 1.5px; color: var(--gold); font-weight: 600;
  }
</style>
</head>
<body>

  <div class="neck-label">
    <div class="neck-band"></div>
    <div class="neck-title">Gran Reserva</div>
    <div class="neck-sub">Very Special<br>Pot Still</div>
    <div class="neck-script" role="img" aria-label="Hand-lettered word Brandy"></div>
  </div>

  <div class="main-label">
    <div class="brand-band" role="img" aria-label="Dark band with subtle ornamental pattern">
      <div class="origin-square"></div>
      <div class="brand-name">Velintor</div>
      <div class="brand-tag">SWISS DISTILLERY</div>
    </div>

    <h1 class="product-title">Gran Reserva</h1>
    <p class="product-sub">Very Special Pot Still</p>
    <div class="script-word" role="img" aria-label="Silver hand-lettered word Brandy"></div>

    <div class="info-card">
      <p class="story">This brandy is crafted from carefully selected grapes, distilled in Copper Pot Stills, and aged for at least 6 years in French Oak Barrels. The long aging process allows the Brandy to develop complex flavors and a smooth, rich character.</p>
      <div class="age-mark">
        <span class="age-word">Aged</span>
        <span class="age-num">6</span>
        <span class="age-word">Years</span>
      </div>
      <ul class="tasting">
        <li><b>Colour:</b> rich golden colour</li>
        <li><b>Aroma:</b> ripe apple with hints of vanilla</li>
        <li><b>Taste:</b> spicy with fruity palate</li>
        <li><b>Finish:</b> well balanced with a fruity aftertaste</li>
      </ul>
      <div class="barrel-line">
        <span>Aged In French</span>
        <span class="barrel-icon" role="img" aria-label="Oak barrels illustration"></span>
        <span>Oak Barrels</span>
      </div>
      <div class="volume">45% Alc. Vol. &nbsp;|&nbsp; 750 ml</div>
    </div>
    <div class="wax-seal" role="img" aria-label="Red wax seal: hand-crafted small batch"></div>

    <p class="producer">Produced by Velintor Swiss Distillery, Switzerland</p>
  </div>

</body>
</html>
```